Logo is done, need templates now

I want to be able to have an email template, same for word documents, powerpoint etc. I have the logo, now I need all the pieces for appearance in correspondence and marketing

Target Market(s)

Professional Advisors and Wealthy Clients

Font styles to use
Serif

Requirements
Must have
• I want to be able to do word documents and email them with letterhead. I need great email signatures. I need similar formatting for the word documents to be flexible to add to powerpoint and other presentations.

```html
<!DOCTYPE html>
<html lang="en">
<head>
<meta charset="utf-8">
<title>Hollowell Trust — Letterhead</title>
<link rel="stylesheet" href="https://fonts.googleapis.com/css2?family=Cormorant+Garamond:wght@500&family=Didact+Gothic&family=Poppins:wght@400;500&display=swap">
<style>
  :root {
    --backdrop: #e4e4e4;
    --paper: #f9f9f9;
    --ink: #1c1c1c;
    --text: #5a5a5a;
    --greeting: #4a4a4a;
    --rule: #222222;
    --signature-tone: #d2d4d8;
  }
  * { margin: 0; padding: 0; box-sizing: border-box; }
  html, body { width: 1029px; height: 1200px; overflow: hidden; }
  body { background: var(--backdrop); position: relative; }

  .letterhead {
    position: absolute;
    left: 88px; top: 0;
    width: 852px; height: 1200px;
    background: var(--paper);
  }

  .brand-name {
    position: absolute;
    right: 76px; top: 142px;
    font-family: "Cormorant Garamond", serif;
    font-weight: 500;
    font-size: 21px;
    letter-spacing: 2.6px;
    color: var(--ink);
    text-transform: uppercase;
  }

  .letter-body {
    position: absolute;
    left: 73px; top: 438px;
    width: 707px;
    font-family: "Didact Gothic", sans-serif;
    color: var(--text);
  }
  .greeting {
    font-size: 21px;
    color: var(--greeting);
    margin-bottom: 41px;
  }
  .paragraph {
    font-size: 12.6px;
    line-height: 18.2px;
    text-align: justify;
    margin-bottom: 18.2px;
  }
  .closing {
    font-size: 12.6px;
    margin-top: 36px;
  }
  .signature {
    display: block;
    width: 100px; height: 43px;
    margin-top: 28px;
    background: var(--signature-tone);
    border-radius: 3px;
  }

  .letter-footer {
    position: absolute;
    left: 73px; top: 1175px;
    width: 707px;
    font-family: "Poppins", sans-serif;
    font-size: 13px;
    color: var(--text);
  }
  .contact-block {
    position: absolute; left: 0; bottom: 38px;
    line-height: 16px;
  }
  .contact-line { display: flex; align-items: center; gap: 6px; }
  .contact-line svg { width: 11px; height: 11px; fill: var(--ink); }
  .address-block {
    position: absolute; right: 0; bottom: 38px;
    line-height: 16px; text-align: right;
  }
  .footer-rule {
    position: absolute; left: 0; right: 0; bottom: 30px;
    height: 1.5px; background: var(--rule);
  }
  .website {
    position: absolute; left: 0; bottom: 8px;
    font-weight: 500; color: var(--ink);
  }
</style>
</head>
<body>
  <main class="letterhead">
    <div class="brand-name">Hollowell Trust</div>

    <section class="letter-body">
      <p class="greeting">Dear Mr. Carver,</p>
      <p class="paragraph">Lorem ipsum dolor sit amet, consectetur adipiscing elit. Donec orci purus, luctus vitae dignissim eu, iaculis sed purus. Vivamus faucibus, ipsum nec aliquet viverra, leo mauris condimentum ligula, sit amet sagittis enim ligula quis arcu. Nam egestas tortor id nisi porttitor mattis. In tortor ante, ultricies in suscipit a, tempus non massa. Vivamus et auctor mi. Fusce vel massa nulla. Phasellus nec eros mauris, et scelerisque orci.</p>
      <p class="paragraph">Donec malesuada orci vitae nulla accumsan porta a id massa. Quisque accumsan iaculis magna sit amet fringilla. Maecenas consequat, magna eget tincidunt semper, odio nibh rutrum mi, id feugiat ante nisi eu risus. Vestibulum nunc orci, rhoncus a placerat in, ultricies in mi. Cras mattis varius eros, vel fringilla nisi suscipit eget. Quisque scelerisque sagittis nulla at porttitor.</p>
      <p class="paragraph">Sed id augue vitae urna euismod commodo aliquet a quam. Pellentesque arcu velit, cursus et malesuada ut, consequat et diam. Nullam erat sem, rhoncus id ullamcorper vitae, rhoncus et arcu. In ultricies ultricies nulla, ut rutrum nisi iaculis at. Donec eu magna a metus ornare faucibus. Fusce aliquet faucibus ultricies. Morbi semper, est id tincidunt gravida, sem arcu adipiscing lacus, ac bibendum nulla leo eu purus. Quisque nec diam sed risus consectetur a ccumsan quis quis nibh. Vestibulum id purus lorem.</p>
      <p class="paragraph">It is a long established fact that a reader will be distracted by the readable content of a page when looking at its layout. The point of using Lorem Ipsum is that it has a more-or-less normal distribution of letters, as opposed to using 'Content here, content here', making it look like readable English. Many desktop publishing packages</p>
      <p class="closing">Sincerely,</p>
      <span class="signature" role="img" aria-label="Handwritten signature of the sender"></span>
    </section>

    <footer class="letter-footer">
      <div class="contact-block">
        <div class="contact-line">
          <svg viewBox="0 0 24 24" aria-hidden="true"><path d="M6.6 10.8a15.1 15.1 0 0 0 6.6 6.6l2.2-2.2a1 1 0 0 1 1-.25 11.4 11.4 0 0 0 3.6.57 1 1 0 0 1 1 1V20a1 1 0 0 1-1 1A17 17 0 0 1 3 4a1 1 0 0 1 1-1h3.5a1 1 0 0 1 1 1c0 1.25.2 2.45.57 3.57a1 1 0 0 1-.25 1z"/></svg>
          <span>555-014-2273</span>
        </div>
        <div class="contact-line">
          <svg viewBox="0 0 24 24" aria-hidden="true"><path d="M2 5h20v14H2z M2 5l10 7 10-7" /></svg>
          <span>hello@hollowelltrust.com</span>
        </div>
      </div>
      <div class="address-block">
        <div>2140 Alder Court</div>
        <div>Juneau, Alaska 99801</div>
      </div>
      <div class="footer-rule"></div>
      <div class="website">www.hollowelltrust.com</div>
    </footer>
  </main>
</body>
</html>
```